Post Card Design Bright Lantern Youth

We need a postcard design that will be mailed to all residents offering free pickups of donated clothing. Our foundation is called Bright Lantern Youth, we are a nonprofit charitable organization that provides meals and medical services to children in need in Honduras. Collecting unwanted second-hand clothing generates revenue that helps fund the mission and programs run by our foundation. We would like to offer our pickup services to everyone who has any unwanted reusable clothing.

```html
<!DOCTYPE html>
<html lang="en">
<head>
<meta charset="utf-8">
<title>Bright Lantern Youth – Free Clothing Pickup Postcard</title>
<link href="https://fonts.googleapis.com/css2?family=Open+Sans:ital,wght@0,600;0,700;1,600;1,700&display=swap" rel="stylesheet">
<style>
  :root {
    --brick: #7b3222;
    --paper: #e8eae6;
    --white: #ffffff;
    --leaf: #7cbf2f;
    --olive: #7a7a3e;
    --teal: #2b6367;
    --ink: #111111;
  }
  * { margin: 0; padding: 0; box-sizing: border-box; }
  html, body { width: 800px; height: 1200px; overflow: hidden; background: var(--paper); }
  body { font-family: "Open Sans", Arial, sans-serif; }
  .postcard { position: relative; width: 800px; height: 1200px; background: var(--paper); overflow: hidden; }

  .hero-panel { position: absolute; left: 0; top: 0; width: 522px; height: 700px; background: var(--brick); }
  .hero-photo {
    position: absolute; left: 522px; top: 0; width: 278px; height: 700px;
    background: linear-gradient(160deg, #d9d6cf 0%, #eeece7 35%, #c9c7c1 70%, #b5b2ab 100%);
  }
  .wave { position: absolute; left: 0; top: 620px; width: 800px; height: 90px; }

  .brand-card {
    position: absolute; left: 36px; top: 0; width: 444px; height: 222px;
    background: var(--white); border-radius: 0 0 44px 44px;
    display: flex; align-items: center; justify-content: center;
  }
  .brand-name { color: var(--leaf); font-weight: 700; font-size: 38px; letter-spacing: 0.2px; }

  .headline { position: absolute; left: 46px; top: 238px; color: var(--white); font-weight: 700; }
  .headline-main { display: block; font-size: 68px; line-height: 72px; letter-spacing: 0.3px; }
  .headline-sub { display: block; font-size: 33.5px; line-height: 44px; margin-top: 2px; }
  .headline-rule { position: absolute; left: 47px; top: 362px; width: 434px; height: 4px; background: var(--leaf); }

  .intro { position: absolute; left: 47px; width: 440px; color: var(--white); font-weight: 700; font-size: 22px; line-height: 30px; }
  .intro-mission { top: 384px; }
  .intro-appeal { top: 563px; }

  .pill {
    position: absolute; height: 32px; padding: 0 14px; border-radius: 16px;
    background: var(--olive); color: var(--white); font-style: italic; font-weight: 600;
    font-size: 20px; line-height: 32px;
  }
  .pill-about { left: 48px; top: 724px; }
  .pill-steps { left: 420px; top: 720px; }

  .about { position: absolute; left: 50px; width: 340px; color: var(--ink); font-weight: 600; font-size: 20.5px; line-height: 27px; }
  .about-collect { top: 770px; }
  .about-rely { top: 903px; }

  .steps { position: absolute; left: 422px; top: 772px; width: 370px; list-style: none; }
  .step { position: absolute; left: 0; display: flex; align-items: flex-start; }
  .step-num {
    width: 43px; height: 43px; border-radius: 50%; background: var(--teal); color: var(--white);
    font-weight: 700; font-size: 30px; line-height: 43px; text-align: center; flex: none;
  }
  .step-text { margin-left: 16px; margin-top: 4px; color: var(--ink); font-weight: 600; font-size: 20.5px; line-height: 27px; white-space: nowrap; }
  .step-1 { top: 0; }
  .step-2 { top: 73px; }
  .step-3 { top: 147px; }

  .footer { position: absolute; left: 0; top: 1052px; width: 800px; height: 148px; background: var(--teal); }
  .footer-label { position: absolute; left: 23px; top: 19px; color: var(--white); font-weight: 700; font-size: 19px; line-height: 26px; }
  .footer-phone { position: absolute; left: 21px; top: 37px; color: var(--white); font-weight: 700; font-size: 57px; line-height: 70px; letter-spacing: -0.5px; }
  .footer-web { position: absolute; left: 23px; top: 98px; color: var(--leaf); font-weight: 700; font-style: italic; font-size: 22px; line-height: 30px; }
  .footer-art {
    position: absolute; left: 450px; top: 12px; width: 292px; height: 122px; border-radius: 10px;
    background: linear-gradient(90deg, #b9a4d6 0%, #f4b3b0 35%, #f08a6a 55%, #9fd3c0 75%, #f3e2a8 100%);
  }
</style>
</head>
<body>
<main class="postcard">
  <div class="hero-panel"></div>
  <div class="hero-photo" role="img" aria-label="Photo of white baby clothes and a knit cap laid on a grey blanket"></div>
  <svg class="wave" viewBox="0 0 800 90" preserveAspectRatio="none" aria-hidden="true">
    <path d="M0 44 C 100 50, 180 60, 280 58 C 380 56, 460 30, 540 30 C 640 30, 720 56, 800 64 L800 90 L0 90 Z" fill="var(--paper)"/>
  </svg>

  <header class="brand-card">
    <span class="brand-name">Bright Lantern Youth</span>
  </header>

  <h1 class="headline">
    <span class="headline-main">FREE PICKUP</span>
    <span class="headline-sub">OF DONATED CLOTHING!</span>
  </h1>
  <div class="headline-rule"></div>

  <p class="intro intro-mission">We are a nonprofit charitable organization that provides meals and medical services to children in need in Honduras. Your donated clothing helps fund our mission and programs.</p>
  <p class="intro intro-appeal">By donating your unwanted reusable clothing, you are directly supporting our efforts to make a difference.</p>

  <h2 class="pill pill-about">More About Us:</h2>
  <p class="about about-collect">Bright Lantern Youth collects unwanted second-hand clothing to generate revenue that helps fund our programs.</p>
  <p class="about about-rely">We rely on the generosity of our community to provide essential services to children<br>in need.</p>

  <h2 class="pill pill-steps">How to Schedule a Pickup:</h2>
  <ol class="steps">
    <li class="step step-1"><span class="step-num">1</span><span class="step-text">Call or visit our website.</span></li>
    <li class="step step-2"><span class="step-num">2</span><span class="step-text">Schedule a date and<br>time convenient for you.</span></li>
    <li class="step step-3"><span class="step-num">3</span><span class="step-text">Place your donated clothing<br>outside, and we’ll handle<br>the rest!</span></li>
  </ol>

  <footer class="footer">
    <p class="footer-label">Contact Us for Free pickup:</p>
    <p class="footer-phone">(000)-000-0000</p>
    <p class="footer-web">www.brightlanternyouth.org</p>
    <div class="footer-art" role="img" aria-label="Illustration of colourful children's clothes: overalls, dresses, a onesie, socks and pants"></div>
  </footer>
</main>
</body>
</html>
```